Business card design needed

New company based in Brisbane, Australia. Brindle Systems. The business is focused on the delivery of network architecture design and deployment. We will provide both services and the sale of the necessary equipment to deliver the service. Cloud computing is an important element of our focus as this is an emerging market for enterprises in Queensland. Our target marketplace is medium to large corporations with complex infrastructure requirements. IT Management and above will be the typical entry point for us into these accounts. We would like to see the use of various shade of green, design should be clutter free and impress stability, trust and growth.
Updates
Hey Everyone
Just we let you all know we have changed this project to 'committed' payment status.
Looking forward to seeing the designs! Thanks for your efforts.
Best Regards
Marcus
Industry/Entity Type
Architecture
Contact Information for Business Card
Brindle Systems, Marcus Doyle, Sales Director, Level 14 Harlow Tower, 58 Penfold Street, Brisbane QLD 4000, Ph +61 7 3904 2267, M +61 4 4926 1573, E marcus.doyle@brindlesystems-example.com.au
Look and feel
Each slider illustrates characteristics of the customer's brand and the style your logo design should communicate.

```html
<!DOCTYPE html>
<html lang="en">
<head>
<meta charset="utf-8">
<title>Brindle Systems — Business Card</title>
<link href="https://fonts.googleapis.com/css2?family=Michroma&display=swap" rel="stylesheet">
<style>
  :root {
    --stage: #2a2a2c;
    --card-dark: #1d1d1f;
    --card-light: #d6d8d6;
    --accent: #3f9a4f;
    --accent-soft: #6cbf6a;
    --ink-dark: #2b2d2b;
    --ink-light: #e4e6e4;
    --texture: #232523;
  }
  * { margin: 0; padding: 0; box-sizing: border-box; }
  html, body {
    width: 1200px;
    height: 900px;
    overflow: hidden;
    background: var(--stage);
    font-family: "Michroma", "Helvetica Neue", Arial, sans-serif;
  }
  .stage {
    position: relative;
    width: 1200px;
    height: 900px;
  }
  .card {
    position: absolute;
    top: 305px;
    width: 520px;
    height: 290px;
    overflow: hidden;
    box-shadow: 0 18px 40px rgba(0,0,0,0.45);
  }

  /* Contact side */
  .card--contact { left: 60px; background: var(--card-dark); }
  .contact__head {
    position: absolute;
    inset: 0 0 auto 0;
    height: 138px;
    background: var(--card-light);
  }
  .contact__rule {
    position: absolute;
    left: 0; right: 0;
    top: 143px;
    height: 4px;
    background: var(--accent);
  }
  .contact__brand {
    position: absolute;
    left: 34px;
    top: 56px;
    font-size: 26px;
    letter-spacing: 1px;
    color: var(--ink-dark);
    text-transform: uppercase;
    white-space: nowrap;
  }
  .contact__bar {
    position: absolute;
    left: 0;
    top: 160px;
    bottom: 0;
    width: 14px;
    background: var(--accent);
  }
  .contact__details {
    position: absolute;
    left: 36px;
    right: 16px;
    top: 166px;
    color: var(--ink-light);
    font-size: 9px;
    line-height: 1.45;
    letter-spacing: 0.3px;
    text-transform: uppercase;
    white-space: nowrap;
  }
  .contact__name {
    font-size: 15px;
    color: var(--accent-soft);
    letter-spacing: 0.5px;
    line-height: 1.2;
  }
  .contact__role { margin-bottom: 12px; }
  .contact__address { margin-bottom: 12px; }
  .contact__label { color: var(--accent-soft); }

  /* Brand side */
  .card--brand { left: 620px; background: var(--card-dark); }
  .brand__texture {
    position: absolute;
    inset: 0;
    background: var(--texture);
  }
  .brand__bar {
    position: absolute;
    right: 20px;
    top: 0;
    width: 20px;
    height: 190px;
    background: var(--accent);
  }
  .brand__name {
    position: absolute;
    left: 20px; right: 60px;
    top: 114px;
    text-align: center;
    font-size: 27px;
    letter-spacing: 1px;
    color: var(--ink-light);
    text-transform: uppercase;
    white-space: nowrap;
  }
  .brand__web {
    position: absolute;
    left: 0; right: 0;
    top: 228px;
    text-align: center;
    font-size: 11px;
    letter-spacing: 0.5px;
    color: var(--ink-light);
    text-transform: uppercase;
  }
</style>
</head>
<body>
<main class="stage">

  <section class="card card--contact" aria-label="Business card, contact side">
    <div class="contact__head"></div>
    <div class="contact__brand">Brindle Systems</div>
    <div class="contact__rule"></div>
    <div class="contact__bar"></div>
    <div class="contact__details">
      <p class="contact__name">Marcus Doyle</p>
      <p class="contact__role">Sales Director</p>
      <p class="contact__address">Level 14 Harlow Tower, 58 Penfold Street,<br>Brisbane QLD 4000</p>
      <p><span class="contact__label">P:</span> +61 7 3904 2267 <span class="contact__label">M:</span> +61 4 4926 1573</p>
      <p><span class="contact__label">E:</span> marcus.doyle@brindlesystems-example.com.au</p>
    </div>
  </section>

  <section class="card card--brand" aria-label="Business card, brand side">
    <div class="brand__texture" role="img" aria-label="Faint repeated brand-name texture across the dark card"></div>
    <div class="brand__bar"></div>
    <div class="brand__name">Brindle Systems</div>
    <div class="brand__web">www.brindlesystems-example.com.au</div>
  </section>

</main>
</body>
</html>
```